Business Card Design Project

I run holistic health workshops, speaking engagements, group and 1on1 coaching, cooking classes, and am a speaker and presenter on holistic health topics.

I would like professionally designed business cards using the attached logo. I would like the reverse of the cards to use the leaf pattern blown up large across the back of the card as the design. I'd also like to use the words "mind.body.spirit.nutrition" across the backside of the cards.

The front of the cards should contain the following contact details:
Megan Thorsby-Kell
Founder & President
The Harwick Advisory Group
+61 477 392 604
theharwickadvisorygroup@mailbrook.example

Target Market(s)

Corporate HR, Health & wellness businesses, upmarket spas, other businesses in the holistic health & wellness fields looking for a speaker/presenter/workshop leader

Industry/Entity Type

Cooking

Requirements
Must have
• Must use the attached design; must use earth tones in line with the logo (browns/greens/blues/tans)

```html
<!DOCTYPE html>
<html lang="en">
<head>
<meta charset="utf-8">
<title>Harwick Group — Business Card</title>
<link href="https://fonts.googleapis.com/css2?family=Questrial&family=Mulish:wght@700&display=swap" rel="stylesheet">
<style>
  :root {
    --canvas: #e4e4e2;
    --card: #ffffff;
    --charcoal: #4b4b47;
    --ink: #1f1f1f;
    --leaf-light: #b5d67c;
    --leaf: #8bc145;
    --leaf-mid: #5aa546;
    --leaf-deep: #066f40;
    --shadow: rgba(0, 0, 0, 0.28);
  }
  * { margin: 0; padding: 0; box-sizing: border-box; }
  html, body {
    width: 1200px; height: 1000px; overflow: hidden;
    background: var(--canvas);
    font-family: "Questrial", "Century Gothic", sans-serif;
  }
  .card {
    position: absolute;
    background: var(--card);
    box-shadow: 0 6px 14px var(--shadow);
    overflow: hidden;
  }
  .card--front { left: 280px; top: 58px; width: 672px; height: 410px; }
  .card--back  { left: 280px; top: 520px; width: 674px; height: 410px; }

  /* Front */
  .front-glow {
    position: absolute; inset: 0;
    background:
      radial-gradient(ellipse 230px 260px at 40px 330px, var(--leaf-deep) 0%, rgba(6,111,64,0.6) 35%, rgba(6,111,64,0) 75%),
      radial-gradient(ellipse 330px 420px at 80px 200px, var(--leaf) 0%, rgba(139,193,69,0.75) 40%, rgba(139,193,69,0) 85%);
  }
  .brand {
    position: absolute; right: 54px; top: 150px;
    display: flex; align-items: center; gap: 16px;
  }
  .brand__dot {
    width: 34px; height: 34px; border-radius: 50%;
    background: var(--leaf);
  }
  .brand__name {
    font-size: 54px; line-height: 1; letter-spacing: -0.5px;
    color: var(--charcoal);
  }
  .brand__tagline {
    position: absolute; right: 54px; top: 306px;
    font-size: 23px; color: var(--charcoal);
  }

  /* Back */
  .leaf-field {
    position: absolute; left: -40px; top: -40px; width: 420px; height: 340px;
    background:
      radial-gradient(ellipse 80px 200px at 130px 110px, var(--leaf-deep) 0%, rgba(6,111,64,0.85) 55%, rgba(6,111,64,0) 100%),
      radial-gradient(ellipse 200px 170px at 190px 150px, var(--leaf-mid) 0%, var(--leaf) 50%, rgba(181,214,124,0.8) 78%, rgba(181,214,124,0) 100%);
  }
  .contact {
    position: absolute; right: 34px; text-align: right; z-index: 2;
  }
  .contact--person { top: 86px; }
  .contact--reach { top: 256px; }
  .person__name {
    font-family: "Mulish", sans-serif; font-weight: 700;
    font-size: 20px; color: var(--leaf); line-height: 30px;
  }
  .person__role {
    font-family: "Mulish", sans-serif; font-weight: 700;
    font-size: 20px; color: var(--ink); line-height: 30px;
  }
  .person__org, .reach__phone {
    font-size: 21px; color: var(--ink); line-height: 30px;
  }
  .reach__email {
    font-family: "Mulish", sans-serif; font-weight: 700;
    font-size: 19px; color: var(--ink); line-height: 30px;
  }
  .tagline-band {
    position: absolute; left: 0; right: 0; bottom: 0; height: 92px; z-index: 1;
    background:
      linear-gradient(to bottom, rgba(255,255,255,1) 0%, rgba(255,255,255,0) 55%),
      linear-gradient(to right, rgba(255,255,255,0.5) 0%, var(--leaf-deep) 20%, var(--leaf-mid) 45%, var(--leaf) 75%, var(--leaf-light) 100%);
  }
  .tagline {
    position: absolute; right: 30px; bottom: 16px; z-index: 2;
    font-size: 50px; line-height: 1; color: rgba(255,255,255,0.92); letter-spacing: 0.5px;
  }
</style>
</head>
<body>
  <section class="card card--front" aria-label="Card front">
    <div class="front-glow"></div>
    <div class="brand">
      <span class="brand__dot"></span>
      <span class="brand__name">Harwick Group</span>
    </div>
    <p class="brand__tagline">the harwick advisory group</p>
  </section>

  <section class="card card--back" aria-label="Card back">
    <div class="leaf-field" role="img" aria-label="Enlarged green leaf pattern from the brand symbol"></div>
    <div class="contact contact--person">
      <p class="person__name">Megan Thorsby-Kell</p>
      <p class="person__role">founder &amp; president</p>
      <p class="person__org">the harwick advisory group</p>
    </div>
    <div class="contact contact--reach">
      <p class="reach__phone">+61 477 392 604</p>
      <p class="reach__email">theharwickadvisorygroup@mailbrook.example</p>
    </div>
    <div class="tagline-band"></div>
    <p class="tagline">mind.body.spirit.nutrition</p>
  </section>
</body>
</html>
```